Hudson Tech Service, Technology & Security Co.

need a new business card design for our Technology & Security Company. We are a Computer Networking Company, Security Camera Installers, Phone Systems.

Target Market(s)

Construction, Medical, Law Offices, Accounting, Retail etc.

Industry/Entity Type

Information Technology

Logo is attached, colors are Blue, Red, Black. Blue for Technology & Red is for Security Cameras, Access Control, Alarm Systems

Colors
fbed22
ec1f27
0555a3
ffffff

Requirements
Must have
• Pictures or Icons for
• For Technology:
• Computer, Network, Phone System, Copier, TV, Cabling
• For Security:
• Video Surveillance, Access Control, Intercom, Fire Alarm, Burglar Alarm, Time Clock

```html
<!DOCTYPE html>
<html lang="en">
<head>
<meta charset="utf-8">
<title>Hudson Tech Service – Business Card</title>
<link href="https://fonts.googleapis.com/css2?family=Mulish:wght@400;600;800&display=swap" rel="stylesheet">
<style>
  :root{
    --blue:#0a6bb8;
    --red:#e8222b;
    --ink:#1d1d1f;
    --grey:#6b6b6b;
    --rule:#b9b9b9;
    --paper:#ffffff;
    --backdrop:#2b2b2b;
  }
  *{box-sizing:border-box;margin:0;padding:0}
  html,body{width:1200px;height:930px;overflow:hidden}
  body{background:var(--backdrop);font-family:"Mulish",sans-serif;position:relative}

  .card{position:absolute;width:660px;height:378px;background:var(--paper);border-radius:16px;overflow:hidden}
  .card--front{left:70px;top:60px}
  .card--back{left:470px;top:492px}

  .brand{display:flex;align-items:center;gap:10px;font-weight:800;color:var(--ink);font-size:26px;letter-spacing:.5px;text-transform:uppercase}
  .brand__dot{width:14px;height:14px;border-radius:50%;background:var(--red)}
  .card--front .brand{position:absolute;left:0;right:0;top:70px;justify-content:center}
  .card--back .brand{position:absolute;left:40px;top:86px;font-size:24px}

  .services{position:absolute;left:0;right:0;display:grid;grid-template-columns:repeat(6,1fr);gap:3px}
  .services--tech{top:150px}
  .services--security{top:253px}
  .tile{height:100px;display:flex;flex-direction:column;align-items:center;justify-content:center;gap:8px;color:#fff;font-size:13.5px;text-align:center;line-height:1.15}
  .services--tech .tile{background:var(--blue)}
  .services--security .tile{background:var(--red)}
  .tile svg{width:26px;height:26px;fill:none;stroke:#fff;stroke-width:1.8;stroke-linecap:round;stroke-linejoin:round}

  .person{position:absolute;right:46px;top:78px;text-align:right}
  .person__name{font-size:24px;font-weight:600;text-transform:uppercase;color:var(--blue);letter-spacing:.5px}
  .person__name span{color:var(--red)}
  .person__role{font-size:15px;color:var(--grey);margin-top:2px}
  .rule-name{position:absolute;left:250px;right:40px;top:146px;height:1.5px;background:var(--rule)}

  .address{position:absolute;left:40px;top:196px;font-size:15px;color:var(--grey);line-height:1.4;padding-bottom:10px;border-bottom:1.5px solid var(--rule);width:240px}
  .contacts{position:absolute;left:40px;top:260px;list-style:none;font-size:15px;color:var(--grey);line-height:1.45}
  .contacts li{display:flex;align-items:center;gap:12px}
  .contacts svg{width:14px;height:14px;fill:var(--blue)}

  .swoosh{position:absolute;right:0;bottom:0;width:420px;height:230px}
</style>
</head>
<body>

<section class="card card--front" aria-label="Card front">
  <div class="brand"><span class="brand__dot"></span>Hudson Tech Service</div>

  <div class="services services--tech">
    <div class="tile"><svg viewBox="0 0 24 24"><rect x="3" y="4" width="18" height="12" rx="1"/><path d="M9 20h6M12 16v4"/></svg>Computer</div>
    <div class="tile"><svg viewBox="0 0 24 24"><circle cx="12" cy="12" r="10"/><circle cx="8" cy="14" r="1.6"/><circle cx="15" cy="8" r="1.6"/><circle cx="16" cy="15" r="1.6"/><path d="M9.3 13l4.4-4M9.6 14.2l4.8.6"/></svg>Network</div>
    <div class="tile"><svg viewBox="0 0 24 24"><rect x="7" y="2" width="10" height="20" rx="2"/><path d="M11 18h2"/></svg>Phone System</div>
    <div class="tile"><svg viewBox="0 0 24 24"><path d="M7 8V3h10v5"/><rect x="3" y="8" width="18" height="9" rx="1"/><path d="M7 17v4h10v-4M7 12h4"/></svg>Copier</div>
    <div class="tile"><svg viewBox="0 0 24 24"><rect x="2" y="5" width="20" height="12" rx="1"/><path d="M8 21h8"/></svg>TV</div>
    <div class="tile"><svg viewBox="0 0 24 24"><rect x="6" y="3" width="4" height="8" rx="1"/><rect x="14" y="13" width="4" height="8" rx="1"/><path d="M8 11v5a4 4 0 004 4M16 13V8a4 4 0 00-4-4"/></svg>Cabling</div>
  </div>

  <div class="services services--security">
    <div class="tile"><svg viewBox="0 0 24 24"><path d="M4 7l13 3-1.5 5L3 12z"/><path d="M15 14l3 4M18 18h3"/></svg>Video<br>Surveillance</div>
    <div class="tile"><svg viewBox="0 0 24 24"><rect x="6" y="2" width="12" height="20" rx="2"/><path d="M9 7h.01M12 7h.01M15 7h.01M9 11h.01M12 11h.01M15 11h.01M9 15h.01M12 15h.01M15 15h.01"/></svg>Access<br>Control</div>
    <div class="tile"><svg viewBox="0 0 24 24"><rect x="6" y="2" width="12" height="20" rx="1.5"/><path d="M9 6h6M9 9h6M10 14h4v4h-4z"/></svg>Intercom</div>
    <div class="tile"><svg viewBox="0 0 24 24"><path d="M7 18v-6a5 5 0 0110 0v6"/><path d="M4 20h16M12 3v2M4 8l1.5 1M20 8l-1.5 1"/></svg>Fire Alarm</div>
    <div class="tile"><svg viewBox="0 0 24 24"><circle cx="12" cy="12" r="2"/><path d="M8 8a5.5 5.5 0 000 8M16 8a5.5 5.5 0 010 8M5 5a9.5 9.5 0 000 14M19 5a9.5 9.5 0 010 14"/></svg>Burglar<br>Alarm</div>
    <div class="tile"><svg viewBox="0 0 24 24"><circle cx="12" cy="12" r="9"/><path d="M12 7v5l3 2"/></svg>Time Clock</div>
  </div>
</section>

<section class="card card--back" aria-label="Card back">
  <div class="brand"><span class="brand__dot"></span>Hudson Tech Service</div>

  <div class="person">
    <div class="person__name">Daniel <span>Reyes</span></div>
    <div class="person__role">Founder</div>
  </div>
  <div class="rule-name"></div>

  <p class="address">4810 Cedar Avenue,<br>Suite C204 Phoenix 85031</p>

  <ul class="contacts">
    <li><svg viewBox="0 0 24 24"><path d="M7 1h10a2 2 0 012 2v18a2 2 0 01-2 2H7a2 2 0 01-2-2V3a2 2 0 012-2zm0 3v14h10V4z"/></svg>800-555-0147</li>
    <li><svg viewBox="0 0 24 24"><path d="M2 5h20v14H2zm2 2v.5l8 5.5 8-5.5V7z"/></svg>dreyes@mailbox.com</li>
    <li><svg viewBox="0 0 24 24"><path d="M12 2a10 10 0 100 20 10 10 0 000-20zm0 3a7 7 0 110 14 7 7 0 010-14zm0 3a4 4 0 100 8 4 4 0 000-8z"/></svg>hudsontechservice.com</li>
  </ul>

  <svg class="swoosh" viewBox="0 0 420 230" preserveAspectRatio="none" aria-hidden="true">
    <path d="M0 230 C140 140 270 60 420 10 L420 20 C280 70 150 150 18 230 Z" fill="var(--red)"/>
    <path d="M28 230 C160 150 290 80 420 38 L420 230 Z" fill="var(--blue)"/>
  </svg>
</section>

</body>
</html>
```